Web design - holistic filmmaker

I need a design for my new website.

I am a holistic filmmaker, ie I make films for healers, alternative practitioners, spiritual people and institutions that offer training in this field.

The design should be noble, bright, convey the feeling of space and expanse and have some particularly beautiful color accents.

The structure is: start page, offer, references, about me, imprint.

As an idea for the start page, I thought that either I could introduce myself as a filmmaker and my offer, or we could start right on the start page with the references, ie photos and links to already realized projects.

If you want more information or an exchange, I'd love to hear from you. At the moment I just don't know how to describe it better.

The winner will then be asked to design a logo.

Target Market(s)

healers, alternative practitioners, spiritual people and institutions that offer training in this field

Industry/Entity Type

Film production

Number of Pages Required

3 page

```html
<!DOCTYPE html>
<html lang="en">
<head>
<meta charset="utf-8">
<title>Jonas Verhoek – Holistic Filmmaker</title>
<link href="https://fonts.googleapis.com/css2?family=EB+Garamond:wght@400;500&family=Arimo:wght@400;700&family=Montserrat:wght@400;500;600&display=swap" rel="stylesheet">
<style>
:root{
  --green:#4f7560;
  --green-dark:#3f6150;
  --bar:#5b7d68;
  --ink:#2c2c2c;
  --muted:#8a8a8a;
  --page:#f8f8f8;
  --band:#efefef;
  --line:#9bb3a5;
  --white:#ffffff;
}
*{margin:0;padding:0;box-sizing:border-box}
html,body{width:1200px;height:4155px;overflow:hidden;background:var(--page)}
body{position:relative;font-family:Arimo,Arial,sans-serif;color:var(--ink)}
.abs{position:absolute}
.serif{font-family:"EB Garamond",Georgia,serif;font-weight:400}

/* top bar */
.topbar{left:0;top:0;width:1200px;height:19px;background:var(--bar);color:var(--white);font-size:9px;display:flex;justify-content:flex-end;align-items:center;gap:10px;padding-right:100px}
.topbar .lang{width:14px;height:14px;border:1px solid #fff;border-radius:50%;font-size:6px;display:flex;align-items:center;justify-content:center}

/* hero */
.hero{left:0;top:19px;width:1200px;height:615px;background:linear-gradient(100deg,#0d1a10 0%,#1f3322 35%,#3d4b3a 60%,#6b6a5c 75%,#8c6a3a 90%,#4a4238 100%)}
.nav{left:46px;top:19px;width:1116px;height:54px;border-bottom:1px solid rgba(255,255,255,.25)}
.logo{font-family:"EB Garamond",Georgia,serif;font-size:34px;font-weight:500;color:var(--white);letter-spacing:1px}
.nav .logo{left:54px;top:6px;border-bottom:2px solid #fff;line-height:1}
.nav-links{left:0;top:21px;width:1116px;height:20px;font-family:"EB Garamond",Georgia,serif;font-size:10px;letter-spacing:.5px;color:var(--white);font-weight:500}
.nav-links span{position:absolute;top:0;white-space:nowrap}
.nav-links .active::after{content:"";position:absolute;left:12px;top:16px;border:4px solid transparent;border-bottom-color:#fff}
.search{left:1024px;top:13px;width:27px;height:27px;border-radius:50%;background:var(--bar)}
.hero-sub{left:124px;top:232px;color:var(--white);font-family:Montserrat,Arial,sans-serif;font-size:18px;letter-spacing:3px;display:flex;align-items:center;gap:8px}
.hero-sub b{font-weight:500;font-size:26px}
.hero-sub::after{content:"";width:58px;height:1px;background:#fff;margin-left:4px}
.hero-quote{left:100px;top:268px;color:var(--white);font-size:48px;line-height:60px}
.hero-quote .cap{font-size:82px}
.btn-outline{left:127px;top:444px;width:199px;height:37px;border:1px solid #fff;color:#fff;font-size:13px;font-family:Montserrat,Arial,sans-serif;font-weight:600;letter-spacing:1.5px;display:flex;align-items:center;justify-content:center;gap:8px}
.arrow{display:inline-block;width:30px;height:2px;background:currentColor;position:relative}
.arrow::after{content:"";position:absolute;right:-1px;top:-4px;border:5px solid transparent;border-left:7px solid currentColor;border-right:0}

/* section title */
.title{color:var(--green);font-family:"EB Garamond",Georgia,serif;font-weight:400;font-size:34px;display:flex;align-items:flex-end;gap:14px;line-height:1}
.title .cap{font-size:82px;line-height:.8;font-weight:400}
.title .rule{width:68px;height:1px;background:var(--line);margin-bottom:6px}
.body-text{font-size:10.5px;line-height:20.5px;color:var(--muted)}

/* intro */
.divider{left:605px;top:612px;width:1px;height:40px;background:#bbb}
.divider-dot{left:598px;top:646px;width:16px;height:16px;border:1px solid var(--green);transform:rotate(45deg)}
.faint-bg{left:860px;top:640px;width:520px;height:650px;border-radius:50%;background:radial-gradient(circle,rgba(220,220,220,.35),rgba(240,240,240,0) 70%)}
.mandala{left:60px;top:705px;width:480px;height:484px;border-radius:50%;background:radial-gradient(circle,#8fa898 0%,#bccabf 45%,#dfe6e0 75%,rgba(248,248,248,0) 100%)}
.intro-title{left:621px;top:775px;flex-direction:column;align-items:flex-start;gap:0}
.intro-text{left:624px;top:900px;width:476px}

/* about */
.about-title{left:100px;top:1290px}
.about-text{left:100px;top:1395px;width:580px}
.awards{left:92px;top:1625px;display:flex;gap:24px;font-size:10.5px;font-weight:700;color:#444}
.award{display:flex;flex-direction:column;align-items:center;gap:8px}
.award svg{width:44px;height:36px}
.link-more{font-family:Montserrat,Arial,sans-serif;font-size:12px;font-weight:500;letter-spacing:1.5px;color:var(--green);display:flex;align-items:center;gap:6px;white-space:nowrap}
.link-more .t{text-decoration:underline;text-underline-offset:3px}
.circle-arrow{width:42px;height:42px;border:1px solid var(--green);border-radius:50%;margin-left:-22px}
.contact-me{left:99px;top:1703px}
.about-band{left:768px;top:1374px;width:432px;height:412px;background:var(--band)}
.about-photo{left:716px;top:1295px;width:381px;height:444px;background:linear-gradient(160deg,#6b7a6a 0%,#9a8a7a 40%,#b07e4a 75%,#d98a2a 100%);box-shadow:0 6px 18px rgba(0,0,0,.15)}

/* references */
.ref-title{left:97px;top:1845px}
.ref-band{left:0;top:2073px;width:1200px;height:492px;background:var(--band)}
.ref-card{box-shadow:0 6px 16px rgba(0,0,0,.2)}
.ref-1{left:0;top:1990px;width:226px;height:425px;background:linear-gradient(120deg,#222 0%,#666 50%,#ccc 100%)}
.ref-2{left:248px;top:2029px;width:321px;height:424px;background:linear-gradient(160deg,#6f8a5a 0%,#3b4a32 45%,#5c5240 100%)}
.ref-3{left:595px;top:1990px;width:321px;height:425px;background:linear-gradient(120deg,#d8d8d8 0%,#8a8a8a 55%,#555 100%)}
.ref-name{font-family:"EB Garamond",Georgia,serif;font-size:22px;color:#555;text-align:center;white-space:nowrap}
.ref-more{justify-content:center}

/* testimonials */
.testi-title{left:468px;top:2660px}
.testi-quote{left:574px;top:2638px;font-family:"EB Garamond",Georgia,serif;font-size:60px;color:var(--green);line-height:1}
.testi-text{left:155px;top:2782px;width:890px;text-align:center}
.avatar{left:570px;top:2886px;width:60px;height:60px;border-radius:50%;background:linear-gradient(#c9c9c9,#7d7d7d);border:2px solid #fff;box-shadow:0 2px 6px rgba(0,0,0,.2)}
.pager{left:480px;top:2973px;width:240px;height:36px;font-family:Montserrat,Arial,sans-serif;font-size:12px;letter-spacing:1.5px;color:#666}
.pager .prev{position:absolute;left:0;top:10px;display:flex;align-items:center;gap:6px}
.pager .sep{position:absolute;left:119px;top:0;width:1px;height:36px;background:#bbb}
.pager .next{position:absolute;left:158px;top:10px;display:flex;align-items:center;gap:6px;color:var(--green)}
.pager .next .t{text-decoration:underline}
.arrow.sm{width:22px;height:1px}
.arrow.left{transform:scaleX(-1)}

/* blog */
.blog-title{left:100px;top:3117px}
.blog-1{left:140px;top:3257px;width:391px;height:319px;background:linear-gradient(135deg,#1a1a1a 0%,#8c8c8c 50%,#2a2a2a 100%)}
.blog-2{left:569px;top:3257px;width:391px;height:363px;background:linear-gradient(160deg,#6a5a5a 0%,#3a3535 45%,#8a3a2a 100%)}
.blog-3{left:1000px;top:3281px;width:200px;height:323px;background:linear-gradient(135deg,#3a3a3a 0%,#6a5a50 60%,#a04030 100%)}
.blog-overlay{left:569px;top:3450px;width:391px;text-align:center;color:#fff}
.blog-overlay .h{font-family:"EB Garamond",Georgia,serif;font-size:24px;letter-spacing:.5px}
.blog-overlay p{font-size:10px;line-height:19px;margin-top:6px}
.btn-solid{left:695px;top:3544px;width:153px;height:32px;background:var(--green);color:#fff;font-family:Montserrat,Arial,sans-serif;font-size:12px;font-weight:600;letter-spacing:1.5px;display:flex;align-items:center;justify-content:center;gap:8px;border:1px solid #fff}

/* footer */
.footer{left:0;top:3750px;width:1200px;height:380px;background:var(--band)}
.footer .logo{position:absolute;left:0;width:1200px;top:68px;text-align:center;color:var(--green);font-size:30px}
.footer .logo span{border-bottom:2px solid var(--green)}
.f-head{font-family:Montserrat,Arial,sans-serif;font-size:11px;letter-spacing:1.8px;color:#666;font-weight:500}
.f-col{top:183px}
.f-list{list-style:none;margin-top:15px;font-size:10.5px;color:#999}
.f-list li{height:23.4px;display:flex;align-items:flex-start;gap:10px}
.f-list.dots li::before{content:"";width:7px;height:7px;border-radius:50%;background:var(--green);margin-top:3px;flex:none}
.f-news p{font-size:10.5px;line-height:20px;color:#999;margin-top:15px;width:330px}
.f-input{margin-top:22px;width:340px;height:36px;border-bottom:1px solid #ccc;position:relative;font-size:11.5px;color:#aaa;padding-top:8px}
.f-input .go{position:absolute;right:0;top:0;width:36px;height:32px;background:var(--green);display:flex;align-items:center;justify-content:center;color:#fff}
.f-social{margin-top:24px;font-size:10.5px;font-weight:700;color:#444;display:flex;gap:22px;white-space:nowrap}
.f-contact svg{width:12px;height:12px;flex:none;margin-top:1px}
.bottombar{left:0;top:4130px;width:1200px;height:25px;background:var(--bar);color:#fff;font-size:10px;display:flex;align-items:center;justify-content:center}
</style>
</head>
<body>

<div class="abs topbar">
  <span>☎ +123456789 / +1234567890</span>
  <span>✉ hello@example.com</span>
  <span class="lang">DE</span><span class="lang">EN</span>
</div>

<section>
  <div class="abs hero" role="img" aria-label="Portrait photograph of the filmmaker outdoors against a dark green background"></div>
  <div class="abs nav">
    <div class="abs logo">LOGO</div>
    <div class="abs nav-links">
      <span class="active" style="left:445px">HOME</span>
      <span style="left:526px">ABOUT ME</span>
      <span style="left:621px">PORTFOLIO</span>
      <span style="left:734px">OFFERS</span>
      <span style="left:824px">REFERENCES</span>
      <span style="left:941px">IMPRINT</span>
    </div>
    <div class="abs search">
      <svg viewBox="0 0 27 27" width="27" height="27"><circle cx="12" cy="12" r="5" fill="none" stroke="#fff" stroke-width="1.6"/><line x1="16" y1="16" x2="19.5" y2="19.5" stroke="#fff" stroke-width="1.6"/></svg>
    </div>
  </div>
  <div class="abs hero-sub"><span><b>J</b>onas <b>V</b>erhoek- <b>A</b> <b>H</b>olistic <b>F</b>ilmmaker</span></div>
  <div class="abs hero-quote serif">“ <span class="cap">M</span>aking a movie is always<br>&nbsp;&nbsp;a journey to yourself ”</div>
  <div class="abs btn-outline">View All My Work <span class="arrow"></span></div>
</section>

<section>
  <div class="abs divider"></div>
  <div class="abs divider-dot"></div>
  <div class="abs faint-bg"></div>
  <div class="abs mandala" role="img" aria-label="Sage green floral mandala illustration"></div>
  <h2 class="abs title intro-title"><span><span class="cap">S</span>tories For Open</span><span style="display:flex;align-items:flex-end;gap:14px">Hearts<span class="rule"></span></span></h2>
  <p class="abs body-text intro-text">Making a movie is always a journey to yourself. With simple means and without special effects, I accompany you on the way to portraying your essence. A documentary commercial film close to the people. Stories for Open Hearts is aimed at all people and institutions whose striving for truthfulness is the driving force behind their actions.High-quality image design and the informative and comprehensible communication of complex issues are the passion and basis of my image films and company presentations.As a full-service provider,<br>I offer everything from one source, from consulting and conception to the finished film.</p>
</section>

<section>
  <h2 class="abs title about-title"><span><span class="cap">A</span>bout Jonas</span><span class="rule"></span></h2>
  <div class="abs body-text about-text">
    <p>My name is Jonas and I do movies - with enthusiasm and wholeheartedly. I am a holistic filmmaker. At the end of the 1990s, I was faced with the question of whether I should go into alternative medicine or the film industry as a career. Professionally, I chose film at that time, but the spiritual and my passion for the so-called alternative healing methods have accompanied me almost as intensely ever since.</p>
    <p style="margin-top:20px">My cinematic path literally brought me from cable guy to cameraman, director and producer. It all started in 1995 as a camera assistant for the US news agency NWX. In the following years, I worked in various positions on numerous national and international television productions, cinema and documentary films, commercials and live productions.Working in the documentary field was the most defining for my career. The insights into the manifold life stories of the people involved and the cinematic way of storytelling fascinated me the most - and I still follow this ap-</p>
  </div>
  <div class="abs awards">
    <div class="award"><svg viewBox="0 0 44 36"><circle cx="22" cy="18" r="12" fill="none" stroke="#444" stroke-width="1.5"/><path d="M22 11l2.2 4.5 5 .7-3.6 3.5.9 5L22 22.3l-4.5 2.4.9-5-3.6-3.5 5-.7z" fill="#444"/></svg>Festival Winner</div>
    <div class="award"><svg viewBox="0 0 44 36"><path d="M14 6v16a8 8 0 0 0 8 8 8 8 0 0 0 8-8V6" fill="none" stroke="#444" stroke-width="1.5"/><line x1="22" y1="10" x2="22" y2="26" stroke="#444" stroke-width="1.5"/></svg>Best Film Maker</div>
    <div class="award"><svg viewBox="0 0 44 36"><circle cx="22" cy="18" r="13" fill="none" stroke="#444" stroke-width="1.5" stroke-dasharray="3 2"/><path d="M22 11l2.2 4.5 5 .7-3.6 3.5.9 5L22 22.3l-4.5 2.4.9-5-3.6-3.5 5-.7z" fill="#444"/></svg>Best Academy Awards</div>
  </div>
  <div class="abs link-more contact-me"><span class="t">Contact Me</span><span class="arrow"></span><span class="circle-arrow"></span></div>
  <div class="abs about-band"></div>
  <div class="abs about-photo" role="img" aria-label="Portrait photograph of the filmmaker in an orange and grey jacket"></div>
</section>

<section>
  <h2 class="abs title ref-title"><span><span class="cap">R</span>eferences</span><span class="rule"></span></h2>
  <div class="abs ref-band"></div>
  <div class="abs ref-card ref-1" role="img" aria-label="Black and white still of a woman from a live stream"></div>
  <div class="abs ref-card ref-2" role="img" aria-label="Film still of a speaker at a lectern outdoors"></div>
  <div class="abs ref-card ref-3" role="img" aria-label="Black and white still of a woman in front of a whiteboard"></div>
  <div class="abs ref-name" style="left:-6px;top:2436px">ve Streams</div>
  <div class="abs link-more" style="left:-4px;top:2472px"><span class="t">ow More</span><span class="arrow"></span></div>
  <div class="abs ref-name" style="left:248px;top:2476px;width:321px">Documentaries</div>
  <div class="abs link-more ref-more" style="left:248px;top:2510px;width:321px"><span class="t">Know More</span><span class="arrow"></span></div>
  <div class="abs ref-name" style="left:605px;top:2436px;width:321px">Advertising Films</div>
  <div class="abs link-more ref-more" style="left:605px;top:2472px;width:321px"><span class="t">Know More</span><span class="arrow"></span></div>
  <div class="abs link-more" style="left:981px;top:2212px"><span>See All</span><span class="arrow"></span><span class="circle-arrow"></span></div>
</section>

<section>
  <div class="abs testi-quote">“</div>
  <h2 class="abs title testi-title"><span><span class="cap">T</span>estimonials</span><span class="rule" style="width:58px"></span></h2>
  <p class="abs body-text testi-text">Sed ut perspiciatis unde omnis iste natus error sit voluptatem accusantium doloremque laudantium, totam rem aperiam, eaque ipsa quae ab illo inventore veritatis et quasi architecto beatae vitae dicta sunt explicabo. Nemo enim ipsam voluptatem quia voluptas sit aspernatur aut odit aut fugit, sed quia consequuntur magni dolores eos qui ratione voluptatem sequi nesciunt. Neque porro quisquam est, qui dolorem ipsum quia dolor sit amet, consectetur, adipisci velit, sed quia non numquam eius modi tempora incidunt ut labore et dolore magnam aliquam quaerat voluptatem.</p>
  <div class="abs avatar" role="img" aria-label="Small portrait of the client giving the testimonial"></div>
  <div class="abs pager">
    <span class="prev"><span class="arrow sm left"></span>Prev</span>
    <span class="sep"></span>
    <span class="next"><span class="t">Next</span><span class="arrow sm"></span></span>
  </div>
</section>

<section>
  <h2 class="abs title blog-title"><span><span class="cap">L</span>atest Blog</span><span class="rule" style="width:58px"></span></h2>
  <div class="abs link-more" style="left:981px;top:3147px"><span>See All</span><span class="arrow"></span><span class="circle-arrow"></span></div>
  <div class="abs blog-1" role="img" aria-label="Black and white photograph of a laughing man"></div>
  <div class="abs blog-2" role="img" aria-label="Photograph of a film crew with camera equipment during an interview shoot"></div>
  <div class="abs blog-3" role="img" aria-label="Photograph of a man reviewing footage"></div>
  <div class="abs blog-overlay">
    <div class="h">Interviews</div>
    <p>I offer everything from one source , from consulting<br>and conception to the finished film</p>
  </div>
  <div class="abs btn-solid">Know More <span class="arrow"></span></div>
</section>

<footer class="abs footer">
  <div class="logo"><span>LOGO</span></div>
  <div class="abs f-col f-news" style="left:102px">
    <div class="f-head">SUBSCRIBE TO OUR NEWSLETTER</div>
    <p>Sed ut perspiciatis unde omnis iste natus error sit voluptatem accusantium doloremque laudantium, totam rem aperiam,</p>
    <div class="f-input">email@example.com<span class="go"><span class="arrow" style="width:18px"></span></span></div>
    <div class="f-social"><span>TW.</span><span>VI.</span><span>YT.</span><span>IN.</span><span style="margin-left:40px">Tax ID Number: 123-459-789</span></div>
  </div>
  <div class="abs f-col" style="left:513px">
    <div class="f-head">PAGES</div>
    <ul class="f-list dots"><li>About Me</li><li>Offers</li><li>References</li><li>Portfolio</li><li>Services</li><li>Legal</li></ul>
  </div>
  <div class="abs f-col" style="left:692px">
    <div class="f-head">QUICK LINK</div>
    <ul class="f-list dots"><li>Privacy Policy</li><li>Terms &amp; Conditions</li><li>FAQ</li><li>Latest Video</li></ul>
  </div>
  <div class="abs f-col" style="left:890px">
    <div class="f-head">CONTACT / IMPRINT</div>
    <ul class="f-list f-contact">
      <li style="height:46px"><svg viewBox="0 0 12 12"><path d="M6 1a3.5 3.5 0 0 0-3.5 3.5C2.5 7 6 11 6 11s3.5-4 3.5-6.5A3.5 3.5 0 0 0 6 1z" fill="#555"/><circle cx="6" cy="4.5" r="1.2" fill="#efefef"/></svg><span style="line-height:20px;margin-top:-4px">Loremipsum dolor sit vero eos et<br>accusamus.</span></li>
      <li><svg viewBox="0 0 12 12"><rect x="1" y="5" width="10" height="6" rx="1" fill="#555"/><path d="M1 5c0-3 10-3 10 0" fill="none" stroke="#555" stroke-width="1.5"/></svg>+123456789</li>
      <li><svg viewBox="0 0 12 12"><path d="M2 1l2.5 0 1 3-1.5 1a6 6 0 0 0 3 3l1-1.5 3 1V10a1 1 0 0 1-1 1A9 9 0 0 1 1 2a1 1 0 0 1 1-1z" fill="#555"/></svg>+1234567890</li>
      <li><svg viewBox="0 0 12 12"><rect x="1" y="2.5" width="10" height="7" fill="#555"/><path d="M1 2.5l5 4 5-4" fill="none" stroke="#efefef" stroke-width="1"/></svg>hello@example.com</li>
    </ul>
  </div>
</footer>
<div class="abs bottombar">© Loremipsum Company.2023 All Rights Reserved.</div>

</body>
</html>
```